Business card for boutique investment firm

Need a business card designed for our boutique investment firm called "BrightLedger Investment Fee Advisors". We help investors achieve lower fees through negotiation on their behalf. We have a logo to work with and a color palette. The card should incorporate our tag line "Clarity in every basis point" and space for relevant details. The look and feel should reflect the logo and our brand personality: Humble, Trustworthy, Friendly

Target Market(s)

High net worth investors who are looking for clarity around how they are being charged by their investment advisor

Industry/Entity Type

Boutique

Requirements
Must have
• Logo
Tag line: Clarity in every basis point
Space for relevant contact details: name, title, phone, email, URL, mailing address

Use these fonts: 'AvantGarde Bk BT' and 'AvantGarde Bk BT Demi'
Use these colors:
Orange = C-0 / M-60 / Y-100 / K-0
Grey = C-0 / M-0 / Y-0 / K-60

```html
<!DOCTYPE html>
<html lang="en">
<head>
<meta charset="utf-8">
<title>BrightLedger Investment Fee Advisors – Business Card</title>
<link href="https://fonts.googleapis.com/css2?family=Poppins:wght@400;600&display=swap" rel="stylesheet">
<style>
  :root {
    --orange: #f26c23;
    --orange-light: #f58a3c;
    --orange-dark: #d95a12;
    --grey: #808285;
    --grey-light: #c9cacc;
    --ink: #555759;
    --white: #ffffff;
    --backdrop: #3b3b3b;
    --font-book: "Poppins", sans-serif;
  }
  * { box-sizing: border-box; margin: 0; padding: 0; }
  html, body { width: 1200px; height: 736px; overflow: hidden; }
  body {
    background: var(--backdrop);
    font-family: var(--font-book);
    position: relative;
  }
  .card {
    position: absolute;
    top: 218px;
    width: 525px;
    height: 300px;
    border-radius: 4px;
    overflow: hidden;
    box-shadow: 0 10px 30px rgba(0,0,0,.45);
  }
  .card--front { left: 45px; background: var(--white); }
  .card--back  { left: 630px; background: linear-gradient(135deg, var(--orange-light), var(--orange) 55%, var(--orange-dark)); }

  /* brand block */
  .brand { position: absolute; display: flex; align-items: center; gap: 12px; }
  .brand__mark { width: 46px; height: 46px; border-radius: 50%; flex: none; }
  .brand__text { display: flex; flex-direction: column; line-height: 1; font-weight: 400; }
  .brand__name { font-size: 34px; letter-spacing: -.5px; }
  .brand__sub  { font-size: 12.5px; letter-spacing: .9px; margin-top: 4px; }
  .tagline { position: absolute; font-size: 8.5px; letter-spacing: 1px; white-space: nowrap; }

  /* front */
  .card--front .brand { left: 112px; top: 48px; }
  .card--front .brand__mark { background: var(--orange); }
  .card--front .brand__name { color: var(--orange); }
  .card--front .brand__sub { color: var(--grey); }
  .card--front .tagline { left: 224px; top: 34px; color: var(--orange); }
  .front__disc {
    position: absolute; left: 380px; top: 86px;
    width: 150px; height: 150px; border-radius: 50%;
    background: rgba(242,108,35,.07);
  }
  .person { position: absolute; left: 32px; top: 150px; }
  .person__name { color: var(--orange); font-weight: 600; font-size: 19px; letter-spacing: .5px; }
  .person__title { color: var(--grey); font-size: 10.5px; letter-spacing: .8px; margin-top: 1px; }

  .contacts { position: absolute; right: 26px; top: 118px; list-style: none; }
  .contacts__item {
    display: flex; align-items: center; justify-content: flex-end; gap: 10px;
    height: 24px; color: var(--ink); font-size: 11.5px;
  }
  .contacts__icon { width: 18px; height: 16px; flex: none; }

  .address-band {
    position: absolute; left: 188px; right: 0; top: 238px; height: 22px;
    background: var(--orange);
    color: var(--white); font-size: 11.5px; letter-spacing: .3px;
    display: flex; align-items: center; padding-left: 10px;
  }
  .base-strip {
    position: absolute; left: 0; right: 0; bottom: 0; height: 40px;
    background: linear-gradient(180deg, #e3e4e5, var(--grey-light));
  }

  /* back */
  .card--back .brand { left: 118px; top: 122px; }
  .card--back .brand__mark { border: 5px solid var(--white); }
  .card--back .brand__name { color: var(--white); }
  .card--back .brand__sub { color: var(--white); opacity: .9; }
  .card--back .tagline { left: 176px; top: 108px; color: var(--white); }
  .back__disc {
    position: absolute; left: 230px; top: 30px;
    width: 240px; height: 240px; border-radius: 50%;
    background: rgba(255,255,255,.06);
  }
</style>
</head>
<body>

  <section class="card card--front" aria-label="Business card front">
    <div class="front__disc"></div>
    <p class="tagline">clarity in every basis point</p>
    <div class="brand">
      <span class="brand__mark"></span>
      <span class="brand__text">
        <span class="brand__name">BrightLedger</span>
        <span class="brand__sub">Investment Fee Advisors</span>
      </span>
    </div>

    <div class="person">
      <p class="person__name">SAM CARTER</p>
      <p class="person__title">Managing Director</p>
    </div>

    <ul class="contacts">
      <li class="contacts__item">sam.carter@brightledger.com
        <svg class="contacts__icon" viewBox="0 0 18 16"><rect x="1" y="2" width="16" height="12" rx="1" fill="var(--orange)"/><path d="M2 3l7 6 7-6" stroke="#fff" stroke-width="1.4" fill="none"/></svg>
      </li>
      <li class="contacts__item">www.brightledger.com
        <svg class="contacts__icon" viewBox="0 0 18 16"><circle cx="9" cy="8" r="7" fill="var(--orange)"/><g stroke="#fff" stroke-width="1" fill="none"><ellipse cx="9" cy="8" rx="3" ry="6.5"/><path d="M2 8h14M3.5 4.5h11M3.5 11.5h11"/></g></svg>
      </li>
      <li class="contacts__item">07 49550318
        <svg class="contacts__icon" viewBox="0 0 18 16"><circle cx="9" cy="8" r="7.5" fill="var(--orange)"/><path d="M5 6c0-1.5 8-1.5 8 0v1h-2V6H7v1H5zM6 8h6l1 4H5z" fill="#fff"/></svg>
      </li>
      <li class="contacts__item">07 49550427
        <svg class="contacts__icon" viewBox="0 0 18 16"><rect x="5" y="1" width="8" height="5" fill="var(--orange)"/><rect x="1" y="6" width="16" height="7" rx="1.5" fill="var(--orange)"/><rect x="5" y="10" width="8" height="5" fill="#fff" stroke="var(--orange)" stroke-width="1"/></svg>
      </li>
    </ul>

    <p class="address-band">Level 2 24 Harbour Lane, Kingsford Qld 4820</p>
    <div class="base-strip"></div>
  </section>

  <section class="card card--back" aria-label="Business card back">
    <div class="back__disc"></div>
    <p class="tagline">Clarity in every basis point</p>
    <div class="brand">
      <span class="brand__mark"></span>
      <span class="brand__text">
        <span class="brand__name">BrightLedger</span>
        <span class="brand__sub">Investment Fee Advisors</span>
      </span>
    </div>
  </section>

</body>
</html>
```